Brixom Vale needs a powerpoint design

We need a powerpoint design for an Information Technology based in Fairfax call "Brixom Vale". We are Information Technology solutions provider for the Federal Government. We develop Talvex, Mobile and Cloud based solutions. We support the Healthcare and Financial sectors of the Government. We would like to see designs that use the colors of our logo. We've attached a copy of our logo. The final design should communicate Information Technology and System Integration with Agile Development.

Target Market(s)

Our target market is the Federal Government and System Integators in the Washington DC area.

Industry/Entity Type

Government

Requirements
Must have
• The powerpoint design must have a professional look.

```html
<!DOCTYPE html>
<html lang="en">
<head>
<meta charset="utf-8">
<title>Brixom Vale – Presentation Template</title>
<link rel="stylesheet" href="https://fonts.googleapis.com/css2?family=Source+Sans+3:wght@300;400;600;700&display=swap">
<style>
  :root{
    --stage:#000;
    --brand-blue:#1573bd;
    --brand-deep:#0d5fa6;
    --brand-navy:#1e4f9e;
    --rule-blue:#3d86c6;
    --paper:#ffffff;
    --ink:#6f6f6f;
    --ink-dark:#333;
    --pill:#cfcfcf;
    --num-blue:#3e78c4;
    --grey-rule:#9a9a9a;
  }
  *{margin:0;padding:0;box-sizing:border-box}
  html,body{width:1200px;height:900px;overflow:hidden;background:var(--stage)}
  body{position:relative;font-family:"Source Sans 3",sans-serif}
  .slide{position:absolute;width:357px;height:275px;background:var(--paper);overflow:hidden}
  .col-1{left:49px}.col-2{left:416px}.col-3{left:791px}
  .row-1{top:187px}.row-2{top:474px}

  .slide-header{position:absolute;left:0;top:0;width:100%;height:29px;background:var(--brand-blue);
    border-bottom:2px solid #fff;box-shadow:0 2px 0 var(--rule-blue)}
  .slide-title{position:absolute;left:23px;top:7px;color:#fff;font-size:13px;font-weight:600;letter-spacing:.2px}
  .slide-footer{position:absolute;left:14px;right:15px;top:250px;border-top:1px solid var(--grey-rule)}
  .page-num{position:absolute;right:0;top:1px;font-size:5px;color:var(--ink)}
  .brand{position:absolute;display:flex;align-items:center;gap:4px;color:var(--brand-navy);font-weight:700;white-space:nowrap}
  .brand .mark{background:var(--brand-navy)}
  .brand-footer{left:0;top:4px;font-size:8px}
  .brand-footer .mark{width:8px;height:8px}

  /* cover */
  .cover-top{position:absolute;left:0;top:0;width:100%;height:210px;
    background:linear-gradient(120deg,#4b93cf 0%,#1d6fb8 45%,#0f5ea8 100%)}
  .cover-band{position:absolute;left:0;top:210px;width:100%;height:42px;background:#fff;border-top:2px solid #b9d3ea}
  .cover-bottom{position:absolute;left:0;top:252px;width:100%;height:23px;border-top:1px solid #8ab5dc;
    background:linear-gradient(90deg,#6aa6d8,#1d6fb8 60%,#0f5ea8)}
  .cover-text{position:absolute;right:22px;top:104px;text-align:right;color:#fff}
  .cover-welcome{font-size:18px;font-weight:700;line-height:22px}
  .cover-sub{font-size:18px;font-weight:300;line-height:22px}
  .cover-meta{font-size:10.5px;margin-top:6px}
  .brand-cover{left:27px;top:223px;font-size:17px}
  .brand-cover .mark{width:16px;height:16px}

  /* agenda */
  .agenda{position:absolute;left:42px;top:66px;width:267px;height:144px;border:2px solid #c9c9c9;border-radius:6px;
    box-shadow:0 2px 4px rgba(0,0,0,.25);background:#fff;list-style:none;padding-top:11px}
  .agenda li{display:flex;align-items:center;height:18px;margin:0 0 7.5px 10px}
  .agenda .num{width:21px;height:19px;background:var(--num-blue);border:1px solid #2a5ea8;color:#fff;
    font-size:14px;display:flex;align-items:center;justify-content:center;box-shadow:inset 0 0 0 1px #8fb3e2}
  .agenda .item{margin-left:5px;width:216px;height:18px;background:var(--pill);border-radius:3px;
    font-size:8.5px;color:#555;padding-left:9px;line-height:18px}

  /* body text */
  .copy{position:absolute;font-size:6.6px;line-height:12.5px;color:var(--ink);font-weight:300;text-align:justify}
  .photo{position:absolute;border:1px solid #ccc;box-shadow:0 1px 3px rgba(0,0,0,.3)}
  .photo-team{left:39px;top:64px;width:76px;height:91px;background:#fff;padding:3px}
  .photo-team .fill{width:100%;height:100%;background:linear-gradient(160deg,#e9eef3,#8f98a3 55%,#2b2f36)}

  /* team */
  .member{position:absolute;top:82px;width:100px}
  .portrait{width:58px;height:57px;border:3px solid #777;
    background:linear-gradient(180deg,#dfe4ea,#a4adb8 50%,#2c2f35)}
  .member-name{margin-top:16px;color:var(--brand-deep);font-size:8.5px;font-weight:600}
  .member-bio{font-size:5px;line-height:8px;color:#555;margin-top:1px}
  .divider{position:absolute;top:80px;width:1px;height:132px;background:#999}

  /* closing */
  .slide-closing{background:var(--brand-blue)}
  .brand-closing{left:116px;top:142px;color:#fff;font-size:16px}
  .brand-closing .mark{background:#fff;width:14px;height:14px}
</style>
</head>
<body>

<section class="slide col-1 row-1 slide-cover">
  <div class="cover-top"></div>
  <div class="cover-band"></div>
  <div class="cover-bottom"></div>
  <div class="cover-text">
    <div class="cover-welcome">WELCOME</div>
    <div class="cover-sub">TO OUR PRESENTATION</div>
    <div class="cover-meta">Fairhaven, August 25, 2013</div>
  </div>
  <div class="brand brand-cover"><span class="mark"></span>Brixom Vale</div>
</section>

<section class="slide col-2 row-1 slide-agenda">
  <header class="slide-header"><h1 class="slide-title">PRESENTATION TITLE</h1></header>
  <ol class="agenda">
    <li><span class="num">1</span><span class="item">Lorem ipsum dolor sit amet</span></li>
    <li><span class="num">2</span><span class="item">Lorem ipsum dolor sit amet</span></li>
    <li><span class="num">3</span><span class="item">Lorem ipsum dolor sit amet</span></li>
    <li><span class="num">4</span><span class="item">Lorem ipsum dolor sit amet</span></li>
    <li><span class="num">5</span><span class="item">Lorem ipsum dolor sit amet</span></li>
  </ol>
  <footer class="slide-footer"><div class="brand brand-footer"><span class="mark"></span>Brixom Vale</div><span class="page-num">2</span></footer>
</section>

<section class="slide col-3 row-1 slide-text-photo">
  <header class="slide-header"><h1 class="slide-title">PRESENTATION TITLE</h1></header>
  <div class="photo photo-team"><div class="fill" role="img" aria-label="Photo of a smiling business team"></div></div>
  <p class="copy" style="left:126px;top:75px;width:188px">Lorem ipsum dolor sit amet, consectetur adipiscing elit, sed do eiusmod tempor incididunt ut labore et dolore magna aliqua. Ut enim ad minim veniam, quis nostrud exercitation ullamco laboris nisi ut aliquip ex ea commodo consequat. Duis aute irure dolor in reprehenderit in voluptate velit esse cillum dolore eu fugiat nulla pariatur.</p>
  <p class="copy" style="left:39px;top:167px;width:275px">Lorem ipsum dolor sit amet, consectetur adipiscing elit, sed do eiusmod tempor incididunt ut labore et dolore magna aliqua. Ut enim ad minim veniam, quis nostrud exercitation ullamco laboris nisi ut aliquip ex ea commodo consequat. Duis aute irure dolor in reprehenderit in voluptate velit esse cillum dolore eu fugiat nulla pariatur.</p>
  <footer class="slide-footer"><div class="brand brand-footer"><span class="mark"></span>Brixom Vale</div><span class="page-num">2</span></footer>
</section>

<section class="slide col-1 row-2 slide-chart">
  <header class="slide-header"><h1 class="slide-title">PRESENTATION TITLE</h1></header>
  <svg class="pie" width="357" height="275" style="position:absolute;left:0;top:0" aria-label="Pie chart">
    <defs><radialGradient id="pieShadow"><stop offset="0" stop-color="#000" stop-opacity=".25"/><stop offset="1" stop-color="#000" stop-opacity="0"/></radialGradient></defs>
    <ellipse cx="82" cy="220" rx="72" ry="8" fill="url(#pieShadow)"/>
    <path d="M17,166 L17,176 A62,48 0 0 0 141,176 L141,166 Z" fill="#333"/>
    <ellipse cx="79" cy="176" rx="62" ry="48" fill="#333"/>
    <path d="M79,166 L79,118 A62,48 0 1 1 57.8,211.1 Z" fill="#575757"/>
    <path d="M79,166 L57.8,211.1 A62,48 0 0 1 20.7,149.6 Z" fill="#6b6b6b"/>
    <path d="M79,166 L20.7,149.6 A62,48 0 0 1 52.8,122.5 Z" fill="#1565b0"/>
    <path d="M79,166 L52.8,122.5 A62,48 0 0 1 79,118 Z" fill="#5bc0de"/>
  </svg>
  <p class="copy" style="left:162px;top:52px;width:164px">Lorem ipsum dolor sit amet, consectetur adipiscing elit, sed do eiusmod tempor incididunt ut labore et dolore magna aliqua. Ut enim ad minim veniam, quis nostrud exercitation ullamco laboris nisi ut aliquip ex ea commodo consequat. Duis aute irure dolor in reprehenderit in voluptate velit esse cillum dolore eu fugiat nulla pariatur.</p>
  <p class="copy" style="left:162px;top:153px;width:164px">Lorem ipsum dolor sit amet, consectetur adipiscing elit, sed do eiusmod tempor incididunt ut labore et dolore magna aliqua. Ut enim ad minim veniam, quis nostrud exercitation ullamco laboris nisi ut aliquip ex ea commodo consequat. Duis aute irure dolor in reprehenderit in voluptate velit esse cillum dolore eu fugiat nulla</p>
  <footer class="slide-footer"><div class="brand brand-footer"><span class="mark"></span>Brixom Vale</div><span class="page-num">2</span></footer>
</section>

<section class="slide col-2 row-2 slide-team">
  <header class="slide-header"><h1 class="slide-title">PRESENTATION TITLE</h1></header>
  <div class="member" style="left:27px">
    <div class="portrait" role="img" aria-label="Portrait of Martin Hale"></div>
    <div class="member-name">Martin Hale</div>
    <div class="member-bio">President &amp; CEO Eastmoor Oil<br>Director, Norvel Energy<br>CEO, Lumen Power<br>13 years in the deregulated market<br>Graduate of Harlow Law and Wexford</div>
  </div>
  <div class="divider" style="left:119px"></div>
  <div class="member" style="left:132px">
    <div class="portrait" role="img" aria-label="Portrait of Daniel Crane"></div>
    <div class="member-name">Daniel Crane</div>
    <div class="member-bio">COO Eastmoor Oil<br>Director, Norvel Energy<br>CEO, Lumen Power<br>13 years in the deregulated market<br>Graduate of Harlow Law and Wexford</div>
  </div>
  <div class="divider" style="left:228px"></div>
  <div class="member" style="left:242px">
    <div class="portrait" role="img" aria-label="Portrait of Paul Brenner"></div>
    <div class="member-name">Paul Brenner</div>
    <div class="member-bio">VPX Eastmoor Oil<br>Director, Norvel Energy<br>CEO, Lumen Power<br>13 years in the deregulated market<br>Graduate of Harlow Law and Wexford</div>
  </div>
  <footer class="slide-footer"><div class="brand brand-footer"><span class="mark"></span>Brixom Vale</div></footer>
</section>

<section class="slide col-3 row-2 slide-closing">
  <div class="brand brand-closing"><span class="mark"></span>Brixom Vale</div>
</section>

</body>
</html>
```